Environmental Group Website Template

We want a website template for an environmental cause. The website should have a dark content area that is transparent. The website text and icons are white.
The background is a nature scene. The background image repeats.
Industry/Entity Type
Group

```html
<!DOCTYPE html>
<html lang="en">
<head>
<meta charset="utf-8">
<title>Environmental Group – Home</title>
<link rel="stylesheet" href="https://fonts.googleapis.com/css2?family=Comfortaa:wght@400;500&family=Varela+Round&family=Bebas+Neue&family=Open+Sans:wght@400;600&display=swap">
<style>
  :root {
    --sky-top: #1d3f6b;
    --sky-mid: #4d7fae;
    --horizon: #2d4a3a;
    --ground: #1a2a22;
    --water: #0e1c28;
    --bar: #1c1c1c;
    --panel: rgba(22, 18, 14, 0.88);
    --panel-light: rgba(44, 36, 28, 0.88);
    --panel-top: rgba(20, 22, 26, 0.78);
    --accent: #f5a800;
    --accent-light: #ffcf3a;
    --text: #ffffff;
    --nav-text: #e4e0d6;
    --muted: #8c8273;
    --title: #d9f6ff;
    --caption-bg: rgba(70, 66, 60, 0.78);
  }
  * { margin: 0; padding: 0; box-sizing: border-box; }
  html, body { width: 1200px; height: 796px; overflow: hidden; }
  body { position: relative; background: var(--water); font-family: "Open Sans", sans-serif; color: var(--text); }

  .backdrop {
    position: absolute; inset: 0;
    background:
      linear-gradient(180deg, var(--sky-top) 0%, var(--sky-mid) 30%, #6f95b8 44%, var(--horizon) 52%, #3e6a3a 62%, var(--ground) 74%, var(--water) 100%);
  }

  .content {
    position: absolute; left: 190px; top: 84px; width: 821px; height: 712px;
    background: var(--panel);
  }
  .content-top { height: 65px; background: var(--panel-top); }

  .site-header { position: absolute; left: 0; top: 0; width: 1200px; height: 110px; }
  .brand { position: absolute; left: 53px; top: 28px; display: flex; align-items: center; gap: 12px; z-index: 2; }
  .brand-dot { width: 58px; height: 58px; border-radius: 50%; background: var(--accent); }
  .brand-name { font-family: "Comfortaa", sans-serif; font-size: 19px; line-height: 24px; text-align: center; color: var(--nav-text); }
  .nav-bar {
    position: absolute; left: 88px; top: 34px; width: 1032px; height: 50px;
    background: var(--bar); border-radius: 0 25px 25px 0;
    box-shadow: 0 3px 8px rgba(0,0,0,0.5);
  }
  .nav { position: absolute; left: 352px; top: 39px; display: flex; list-style: none; }
  .nav a {
    display: block; padding: 0 7px; height: 41px; line-height: 41px;
    font-family: "Comfortaa", sans-serif; font-size: 20.5px; letter-spacing: 1.1px;
    color: var(--nav-text); text-decoration: none;
  }
  .nav a.is-current {
    background: linear-gradient(180deg, var(--accent-light), var(--accent));
    color: #fff; border-radius: 5px; margin-right: 10px; width: 75px; text-align: center; padding: 0;
  }

  .slider { position: absolute; left: 190px; top: 149px; width: 821px; height: 316px; }
  .slide-image {
    position: absolute; inset: 0 0 21px 0;
    background: linear-gradient(100deg, #6e8fc4 0%, #8aa0c9 30%, #b48a48 50%, #c99a4f 70%, #a77a3a 100%);
  }
  .slide-title {
    position: absolute; left: 24px; top: 16px;
    font-family: "Varela Round", sans-serif; font-weight: 400; font-size: 41px; letter-spacing: 0.5px;
    color: var(--title); text-shadow: 0 0 6px rgba(255,255,255,0.6);
  }
  .slide-arrow { position: absolute; top: 119px; width: 48px; height: 54px; }
  .slide-arrow.prev { left: 13px; }
  .slide-arrow.next { right: 9px; }
  .slide-caption {
    position: absolute; left: 0; bottom: 0; width: 821px; height: 21px;
    background: var(--caption-bg); padding-left: 4px; line-height: 21px;
    font-size: 13px; color: #f0ece4; white-space: nowrap;
  }
  .slide-caption strong { font-weight: 400; font-size: 16px; letter-spacing: 0.3px; }

  .actions { position: absolute; left: 190px; top: 465px; width: 821px; height: 331px; display: flex; }
  .action { width: 274px; text-align: center; position: relative; }
  .action.is-featured { background: var(--panel-light); }
  .action-icon { position: absolute; left: 50%; top: 54px; transform: translateX(-50%); width: 90px; height: 76px; }
  .action h2 {
    position: absolute; top: 142px; width: 100%;
    font-family: "Bebas Neue", sans-serif; font-weight: 400; font-size: 30px; letter-spacing: 2px;
  }
  .action p {
    position: absolute; top: 188px; left: 30px; right: 30px;
    font-family: Arial, sans-serif; font-size: 12.5px; line-height: 14.6px;
  }
  .action a {
    position: absolute; top: 296px; width: 100%; left: 0;
    font-family: "Comfortaa", sans-serif; font-size: 15px; letter-spacing: 1px;
    color: var(--muted); text-decoration: none;
  }
</style>
</head>
<body>
  <div class="backdrop" role="img" aria-label="Nature scene: blue sky with clouds, trees and a calm lake with grassy banks"></div>

  <main class="content">
    <div class="content-top"></div>
  </main>

  <header class="site-header">
    <div class="nav-bar"></div>
    <div class="brand">
      <span class="brand-dot"></span>
      <span class="brand-name">YOUR LOGO<br>HERE</span>
    </div>
    <ul class="nav">
      <li><a class="is-current" href="#">Home</a></li>
      <li><a href="#">About</a></li>
      <li><a href="#">Explore</a></li>
      <li><a href="#">Challenges</a></li>
      <li><a href="#">Solutions</a></li>
      <li><a href="#">Events</a></li>
      <li><a href="#">News</a></li>
    </ul>
  </header>

  <section class="slider">
    <div class="slide-image" role="img" aria-label="Photo of a male lion resting against a blue sky"></div>
    <h1 class="slide-title">SAVE THE LIONS</h1>
    <svg class="slide-arrow prev" viewBox="0 0 48 54" aria-hidden="true"><polygon points="30,0 44,0 18,27 44,54 30,54 4,27" fill="rgba(255,255,255,0.55)"/></svg>
    <svg class="slide-arrow next" viewBox="0 0 48 54" aria-hidden="true"><polygon points="18,0 4,0 30,27 4,54 18,54 44,27" fill="rgba(255,255,255,0.55)"/></svg>
    <div class="slide-caption"><strong>MUMBAI, AFRICA-</strong> Lorem ipsum dolor sit amet, consectetur adipiscing... ▴▴</div>
  </section>

  <section class="actions">
    <article class="action">
      <svg class="action-icon" viewBox="0 0 90 76" aria-hidden="true">
        <circle cx="45" cy="13" r="13" fill="#fff"/>
        <path d="M8 22 L20 16 L38 40 H52 L70 16 L82 22 L62 52 V76 H28 V52 Z" fill="#fff"/>
      </svg>
      <h2>Volunteer</h2>
      <p>Lorem ipsum dolor sit amet, consectetur adipiscing elit. Sed quis fringilla lacus. Maecenas maximus odio id urna pharetra . In sem metus, gravida sed &nbsp;placerat , sagittis enim. Etiam non venenatis nibh.</p>
      <a href="#">Learn More...</a>
    </article>
    <article class="action is-featured">
      <svg class="action-icon" viewBox="0 0 90 76" aria-hidden="true">
        <circle cx="45" cy="38" r="34" fill="none" stroke="#fff" stroke-width="5"/>
        <text x="45" y="53" text-anchor="middle" font-family="Arial, sans-serif" font-size="42" font-weight="700" fill="#fff">$</text>
      </svg>
      <h2>Donate</h2>
      <p>Lorem ipsum dolor sit amet, consectetur adipiscing elit. Sed quis fringilla lacus. Maecenas maximus odio id urna pharetra . In sem metus, gravida sed &nbsp;placerat , sagittis enim. Etiam non venenatis nibh.</p>
      <a href="#">Learn More...</a>
    </article>
    <article class="action">
      <svg class="action-icon" viewBox="0 0 90 76" aria-hidden="true">
        <path d="M14 8 H76 A8 8 0 0 1 84 16 V48 A8 8 0 0 1 76 56 H40 L24 70 V56 H14 A8 8 0 0 1 6 48 V16 A8 8 0 0 1 14 8 Z" fill="#fff"/>
      </svg>
      <h2>Speak Up</h2>
      <p>Lorem ipsum dolor sit amet, consectetur adipiscing elit. Sed quis fringilla lacus. Maecenas maximus odio id urna pharetra . In sem metus, gravida sed &nbsp;placerat , sagittis enim. Etiam non venenatis nibh.</p>
      <a href="#">Learn More...</a>
    </article>
  </section>
</body>
</html>
```